Modern corporate presentation

We need a clean, restrained company presentation in a modern Slidra style (design templates are attached for orientation). Please see the attachment for the briefing, colors and our corporate design.

content 1
Title:

VORLINQ
We connect worlds.
Digitization = increase in customer satisfaction

content 2
Animated on photo of company building (photo attached)

Text:

As Europe's leading service provider for business process outsourcing, we optimize your document management along the entire process chain of your document cycles, including physical long-term archiving after processing - efficiently, flexibly, individually and transparently!

content 3
Title: History
Overview of history as a timeline (see example design template slide 2) with dates and icons
Text:
1995
1997
2000
2016
2018
2021

content 4 or onwards
Morph transitions / individual seasons
1995 Founded by Lothar Brenning
1997 Start of ARKI@NET development
2000 real start ARKI@NET, certification GoB/S and KVR
2016 Development of Big Data + inMemory searches, first processes with AI
2018
ARKI@NET goes mobile
Expansion of the Siegen site with a new logistics center
Launch Pagevault concept
2021 More than 400 satisfied employees

content 5
Title: Facts and Figures
Animated to morph the following texts/numbers:

family business
400 employees at different locations
Own data centers
7,500 pallet spaces
50,000 active users daily on the ARKI@NET platform
525 000 receipts per month
210 customers from all over Europe
all necessary certifications

content 6
Title: Product and service portfolio
Combine yourself...
Create animation from Tobo building blocks, which are put together, morph individually according to the order (1-3).

Module 1:
system platform
• Audit-proof archiving ARKI@NET
• Fully integrated document management
• Complete, certified KVR® integration

Module 2:
solution modules
• Digital files
• Invoice receipt workflow
ordering system
• Digital inbox
• Case management
• Info Cockpit

Module 3:

process services
• Storage
• Scanning Service
• Collection Services
• BPO Inbox
• BPO invoice receipt

content 7
Title: Good Reasons / Benefits
Trust / full-service provider for document-based business processes completely own solution
Portfolio / depiction of the entire process chain from a single source
Experience / reference projects of all sizes and industries
Employees / All services are provided by our own staff without the involvement of subcontractors

content 8
Title: The 100% Philosophy

Overview of the following 3 main points, which are highlighted individually below:

The system
Services
Privacy and Certifications
___

The system
• 100% own data center with 24x7 operation, incl. backup data center
• Certified KVR partner
• Real, completely in-house developed SaaS solution for data center operations only
• Maintenance, support and updates included
• Web-based application

Services
• Combination of man & machine
• Service level agreements, service defined in terms of time
• Penalty for non-fulfilment

Privacy and certifications:
• All common certifications
• Own compliance management
• Data protection according to GDPR

Font styles to use
Other font styles liked:
• Myrlad Pro Bold für Head und Sublines, Lucida Grande Regular für Fließtexte

Requirements
Must have
• clean and reserved, taking our corporate design into account
Nice to have
• Slidra Style, seamless transitions (similar to a glidetrack)

```html
<!DOCTYPE html>
<html lang="de">
<head>
<meta charset="utf-8">
<title>Gute Gründe / Vorteile</title>
<link href="https://fonts.googleapis.com/css2?family=Source+Sans+3:wght@400;600&family=Fira+Sans:wght@400&display=swap" rel="stylesheet">
<style>
  :root{
    --ink:#2b313a;
    --text:#333333;
    --muted:#7a7a7a;
    --rule:#c9c9c9;
    --disc:#f7f7f7;
    --sand:#d3c7a8;
    --charcoal:#3a3a3a;
    --stone:#8a8a8a;
    --silver:#bdbcbc;
    --footer:#29323b;
    --footer-text:#ffffff;
  }
  *{margin:0;padding:0;box-sizing:border-box}
  html,body{width:1200px;height:674px;overflow:hidden;background:#fff}
  .slide{position:relative;width:1200px;height:674px;background:#fff;font-family:"Fira Sans",sans-serif;color:var(--text)}
  .slide-title{position:absolute;top:48px;left:0;width:1200px;text-align:center;font-family:"Source Sans 3",sans-serif;font-weight:600;font-size:33px;color:var(--ink);letter-spacing:-0.2px}
  .title-rule{position:absolute;top:91px;left:117px;width:967px;height:1px;background:var(--rule)}
  .wave{position:absolute;top:0;left:0}
  .step{position:absolute;top:259px;width:164px;height:164px;margin-left:-82px;border-radius:50%;background:var(--disc);text-align:center;font-family:"Source Sans 3",sans-serif}
  .step-num{display:block;margin-top:48px;font-size:17px;color:var(--muted)}
  .step-name{display:block;margin-top:2px;font-size:21px;font-weight:600;color:var(--ink)}
  .step-note{position:absolute;width:150px;margin-left:-75px;text-align:center;font-size:12px;line-height:15.7px;color:var(--text)}
  .footer{position:absolute;left:0;bottom:0;width:1200px;height:67px;background:var(--footer);color:var(--footer-text)}
  .brand{position:absolute;left:120px;top:20px;display:flex;align-items:center;gap:6px;font-family:"Source Sans 3",sans-serif;font-size:22px;letter-spacing:1px;font-weight:400}
  .brand-mark{width:17px;height:17px;background:#fff;border-radius:2px}
  .deck-name{position:absolute;right:164px;top:24px;font-size:14px;letter-spacing:1.4px}
  .footer-divider{position:absolute;left:1049px;top:17px;width:1px;height:50px;background:#fff}
  .page-num{position:absolute;left:1060px;top:17px;font-size:22px}
</style>
</head>
<body>
<main class="slide">
  <h1 class="slide-title">Gute Gründe / Vorteile</h1>
  <div class="title-rule"></div>

  <svg class="wave" width="1200" height="674" viewBox="0 0 1200 674" aria-hidden="true">
    <g fill="none" stroke-width="19" stroke-linecap="butt">
      <path d="M172 345 L172 341 A108 108 0 0 1 388 341" stroke="var(--sand)"/>
      <path d="M388 341 A108 108 0 0 0 604 341" stroke="var(--charcoal)"/>
      <path d="M604 341 A108 108 0 0 1 820 341" stroke="var(--stone)"/>
      <path d="M820 341 A108 108 0 0 0 1036 341" stroke="var(--silver)"/>
    </g>
  </svg>

  <div class="step" style="left:280px"><span class="step-num">01</span><span class="step-name">Vertrauen</span></div>
  <div class="step" style="left:496px"><span class="step-num">02</span><span class="step-name">Portfolio</span></div>
  <div class="step" style="left:712px"><span class="step-num">03</span><span class="step-name">Erfahrung</span></div>
  <div class="step" style="left:928px"><span class="step-num">04</span><span class="step-name">Mitarbeiter</span></div>

  <p class="step-note" style="left:280px;top:436px">Full-Service Provider für dokumentenbasierte Geschäftsprozesse mit vollständig eigener Lösung</p>
  <p class="step-note" style="left:496px;top:180px;width:130px;margin-left:-65px">Abbildung der gesamten Prozesskette aus einer Hand</p>
  <p class="step-note" style="left:712px;top:435px;width:130px;margin-left:-65px">Referenzprojekte in allen Größen und Branchen</p>
  <p class="step-note" style="left:928px;top:164px">Alle Leistungen werden durch eigenes Personal ohne Einbindung von Subunternehmen erbracht</p>

  <footer class="footer">
    <div class="brand"><span class="brand-mark"></span>VORLINQ</div>
    <div class="deck-name">PRESENTATION TITLE</div>
    <div class="footer-divider"></div>
    <div class="page-num">05</div>
  </footer>
</main>
</body>
</html>
```